Visitenkarten für Kfz Sachverständigenbüro - Ingenieurbüro Kolbenrath
Zielgruppe
Erstellung von Unfallgutachten, Oldtimergutachten, Fahrzeugbewertungen, technischen Gutachten etc.
Zielgruppen: Autohäuser, Werkstätten, Oldtimerliebhaber, Privatkunden mit Unfallschäden
Aufgabenstellung
Möglichst beidseitige Visitenkarten mit Firmenlogo integriert, "Firmenfarbe" blau
Ursprüngliche Visitenkarten mit Logo im Anhang

```html
<!DOCTYPE html>
<html lang="de">
<head>
<meta charset="utf-8">
<title>Visitenkarten – Ingenieurbüro Kolbenrath</title>
<link rel="stylesheet" href="https://fonts.googleapis.com/css2?family=Cabin:wght@500&family=Open+Sans:wght@400;700&family=PT+Sans+Narrow&display=swap">
<style>
  :root {
    --brand-blue: #1b2f7e;
    --band-grey: #9b9ca0;
    --muted-grey: #a4a5a8;
    --card-white: #ffffff;
    --canvas-bg: #efeff0;
  }
  * { margin: 0; padding: 0; box-sizing: border-box; }
  html, body { width: 1200px; height: 800px; overflow: hidden; }
  body {
    background: var(--canvas-bg);
    position: relative;
    font-family: "Open Sans", sans-serif;
  }
  .card {
    position: absolute;
    top: 225px;
    width: 550px;
    height: 350px;
    background: var(--card-white);
    overflow: hidden;
  }
  .card--front { left: 35px; }
  .card--back { left: 615px; }

  .card__bands {
    position: absolute;
    left: 0; top: 0;
    width: 550px; height: 350px;
  }
  .band--blue { fill: var(--brand-blue); }
  .band--grey { fill: var(--band-grey); }

  .wordmark {
    position: absolute;
    font-family: "Cabin", sans-serif;
    font-weight: 500;
    color: var(--brand-blue);
    text-align: right;
    line-height: 1;
  }
  .wordmark span { display: block; }
  .card--front .wordmark { right: 71px; top: 90px; }
  .card--front .wordmark__line1 { font-size: 31px; letter-spacing: 0.5px; }
  .card--front .wordmark__line2 { font-size: 52px; margin-top: 6px; letter-spacing: -0.5px; }

  .card--back .wordmark { right: 20px; top: 32px; }
  .card--back .wordmark__line1 { font-size: 14px; }
  .card--back .wordmark__line2 { font-size: 22px; margin-top: 2px; }

  .front__url {
    position: absolute;
    left: 0; right: 0;
    top: 298px;
    text-align: center;
    font-family: "PT Sans Narrow", sans-serif;
    font-size: 27px;
    letter-spacing: 2.5px;
    color: var(--card-white);
    white-space: nowrap;
  }

  .contact {
    position: absolute;
    left: 43px;
    top: 97px;
    font-size: 12.5px;
    letter-spacing: 2px;
    line-height: 16.5px;
    color: var(--brand-blue);
    white-space: nowrap;
  }
  .contact__name { font-weight: 700; letter-spacing: 2.6px; }
  .contact__title { color: var(--muted-grey); }
  .contact__lines { margin-top: 20px; }

  .back__email {
    position: absolute;
    left: 0; right: 0;
    top: 312px;
    text-align: center;
    font-size: 13px;
    font-weight: 700;
    letter-spacing: 2.6px;
    color: var(--card-white);
    white-space: nowrap;
  }
</style>
</head>
<body>

  <section class="card card--front" aria-label="Vorderseite">
    <svg class="card__bands" viewBox="0 0 550 350" aria-hidden="true">
      <path class="band--grey" d="M0,285 H308 C420,288 510,300 550,317 V350 H0 Z"/>
      <path class="band--blue" d="M0,268 H308 C420,272 510,290 550,310 V317 C510,300 420,288 308,285 H0 Z"/>
    </svg>
    <div class="wordmark">
      <span class="wordmark__line1">Ingenieurbüro</span>
      <span class="wordmark__line2">Kolbenrath</span>
    </div>
    <p class="front__url">www.ingbuero-kolbenrath.example</p>
  </section>

  <section class="card card--back" aria-label="Rückseite">
    <svg class="card__bands" viewBox="0 0 550 350" aria-hidden="true">
      <path class="band--grey" d="M0,285 H308 C420,288 510,300 550,317 V350 H0 Z"/>
      <path class="band--blue" d="M0,268 H308 C420,272 510,290 550,310 V317 C510,300 420,288 308,285 H0 Z"/>
    </svg>
    <div class="wordmark">
      <span class="wordmark__line1">Ingenieurbüro</span>
      <span class="wordmark__line2">Kolbenrath</span>
    </div>
    <div class="contact">
      <p class="contact__name">Jonas Kolbenrath</p>
      <p class="contact__title">Dipl.-Ing.(FH) | Kfz-Sachverständiger</p>
      <p class="contact__address">Lindenhofweg 7 | 61234 Talbrunn</p>
      <div class="contact__lines">
        <p>T 06021-4830 &amp; 4831</p>
        <p>F 06021-719 40</p>
        <p>M 0170-000 12 34</p>
        <p>E jonask@ingbuero-kolbenrath.example</p>
      </div>
    </div>
    <p class="back__email">info@ingbuero-kolbenrath.example</p>
  </section>

</body>
</html>
```